A private security company called "Tavrin Security Services Ltd"

Hello everybody,

We need a web page for a company based in NZ. It is mainly an informative website so it would be wonderful if the designer puts their absolute best into making it a website that I would really appreciate. The website needs to show professionalism and also needs to make our web surfers find the information they need in a click. the company's colour is black and silver, and if those two colours could be integrated into the website it would be absolutely lovely. Please do contact me for any information.

Sincerely,
Dorian Velasko

Industry/Entity Type

Security

```html
<!DOCTYPE html>
<html lang="en">
<head>
<meta charset="utf-8">
<title>Tavrin Security Services Ltd</title>
<link rel="stylesheet" href="https://fonts.googleapis.com/css2?family=Archivo+Narrow:wght@400;500;600&family=Arimo:wght@400;700&family=Marcellus+SC&display=swap">
<style>
:root{
  --ink:#1d1d1d;
  --text:#6c6c6c;
  --muted:#8a8a8a;
  --silver-hi:#f6f6f6;
  --silver:#e6e6e6;
  --silver-lo:#cfcfcf;
  --line:#cdcdcd;
  --white:#ffffff;
  --dark:#3a3a3a;
  --darker:#262626;
  --foot-text:#a9a9a9;
  --icon:#b8b8b8;
}
*{margin:0;padding:0;box-sizing:border-box}
html,body{width:1200px;height:2748px;overflow:hidden}
body{position:relative;background:var(--silver-hi);font-family:"Arimo",Arial,sans-serif;color:var(--text)}
.head-font{font-family:"Archivo Narrow","Arial Narrow",sans-serif;font-weight:500;color:var(--ink)}

/* header */
.site-header{position:absolute;left:0;top:0;width:1200px;height:157px;background:linear-gradient(#f5f5f5,#e9e9e9 70%,#d9d9d9);border-bottom:1px solid #c8c8c8}
.brand{position:absolute;left:157px;top:56px;display:flex;align-items:center;gap:10px;font-family:"Arimo",Arial,sans-serif;font-weight:700;font-size:15px;color:var(--ink);line-height:1.15;width:170px}
.brand-dot{width:18px;height:18px;border-radius:50%;background:var(--ink);flex:none}
.tagline{position:absolute;left:418px;top:26px;font-family:"Marcellus SC",serif;font-size:26px;color:var(--ink);letter-spacing:1px;white-space:nowrap}
.main-nav{position:absolute;left:418px;top:100px;display:flex}
.main-nav a{font-family:"Arimo",Arial,sans-serif;font-size:12.5px;color:var(--ink);text-decoration:none;margin-right:42px}
.main-nav a:last-child{margin-right:0}
.socials{position:absolute;display:flex;gap:11px}
.socials span{width:29px;height:29px;border-radius:50%;background:var(--icon);display:block}
.socials.top{left:934px;top:32px}

/* hero */
.hero{position:absolute;left:0;top:158px;width:1200px;height:518px;background:radial-gradient(ellipse at 55% 45%,#bdbdbd,#8f8f8f 45%,#4c4c4c 90%)}
.hero-caption{position:absolute;left:0;top:205px;width:1200px;text-align:center;font-family:"Archivo Narrow",sans-serif;font-size:33px;line-height:42px;color:var(--white)}
.slide-arrow{position:absolute;width:34px;height:34px}
.hero .slide-arrow{top:240px}

/* solutions */
.solutions{position:absolute;left:0;top:676px;width:1200px;height:713px;background:linear-gradient(#f3f3f3,#e4e4e4 60%,#d6d6d6)}
.section-title{position:absolute;left:0;width:1200px;text-align:center;font-size:37px}
.services-nav{position:absolute;left:157px;top:150px;width:212px}
.services-nav h3{font-size:23px;margin-bottom:28px}
.services-nav li{list-style:none;font-size:12.5px;line-height:17px;padding-left:33px;position:relative;margin-bottom:19px;color:var(--muted)}
.services-nav li::before{content:"›";position:absolute;left:5px;top:-2px;font-size:16px;color:#999}
.custom-box{position:absolute;left:157px;top:424px;width:212px;height:251px;background:linear-gradient(#dcdcdc,#9c9c9c);display:flex;flex-direction:column;align-items:center;padding-top:28px}
.custom-box p{font-family:"Archivo Narrow",sans-serif;font-size:24px;line-height:32px;text-align:center;color:#4a4a4a}
.custom-box .box-brand{margin-top:52px;font-family:"Arimo",Arial,sans-serif;font-weight:700;font-size:15px;color:var(--ink);text-align:center;line-height:1.2;padding:0 16px}
.col-line{position:absolute;top:150px;width:1px;height:563px;background:var(--line)}
.row-line{position:absolute;height:1px;background:var(--line)}
.card{position:absolute;width:224px;padding:0 16px}
.card-photo{width:188px;height:104px;border:5px solid var(--white);box-shadow:0 1px 3px rgba(0,0,0,.25)}
.card h4{font-family:"Archivo Narrow",sans-serif;font-weight:500;font-size:19px;color:var(--ink);margin:24px 0 6px}
.card p{font-size:11px;line-height:14px;color:var(--muted)}
.btn{display:block;background:linear-gradient(#fdfdfd,#dadada);border:1px solid #b9b9b9;border-radius:3px;font-size:11.5px;color:#333;text-align:center}
.card .btn{width:68px;height:24px;line-height:22px;margin:10px 0 0 auto}

/* industries */
.industries{position:absolute;left:0;top:1389px;width:1200px;height:402px;background:var(--white)}
.industry{position:absolute;top:145px;width:196px;text-align:center}
.industry .ind-photo{width:196px;height:159px;border:4px solid var(--white);box-shadow:0 1px 4px rgba(0,0,0,.3)}
.industry span{display:block;margin-top:12px;font-family:"Archivo Narrow",sans-serif;font-size:17px;color:var(--ink)}
.industries .slide-arrow{top:205px}

/* solutions split */
.split{position:absolute;left:0;top:1791px;width:1200px;height:483px;background:linear-gradient(#eeeeee,#f8f8f8 50%,#ececec)}
.split-divider{position:absolute;left:600px;top:40px;width:2px;height:390px;background:linear-gradient(rgba(0,0,0,0),rgba(0,0,0,.12),rgba(0,0,0,0))}
.offer{position:absolute;top:78px;width:400px;text-align:center}
.offer .ring{width:184px;height:184px;margin:0 auto;border-radius:50%;background:linear-gradient(#fafafa,#cfcfcf);padding:9px;box-shadow:0 2px 5px rgba(0,0,0,.2)}
.offer .ring div{width:166px;height:166px;border-radius:50%}
.offer h4{font-family:"Archivo Narrow",sans-serif;font-weight:500;font-size:19px;color:var(--ink);margin:22px 0 12px}
.offer p{font-size:11.5px;line-height:15px;color:var(--muted);padding:0 2px}
.offer .btn{width:112px;height:30px;line-height:28px;margin:17px auto 0}

/* footer */
.site-footer{position:absolute;left:0;top:2274px;width:1200px;height:474px;background:linear-gradient(#575757,#2f2f2f 60%,#2a2a2a)}
.site-footer h3{position:absolute;top:50px;font-family:"Archivo Narrow",sans-serif;font-weight:500;font-size:28px;color:var(--white)}
.about-text{position:absolute;left:157px;top:124px;width:305px;font-size:11.5px;line-height:14px;color:var(--foot-text)}
.about-text p+p{margin-top:14px}
.quick-links{position:absolute;left:542px;top:126px;list-style:none}
.quick-links li{font-size:11.5px;line-height:14px;color:var(--foot-text);padding-left:22px;position:relative;margin-bottom:18px;width:130px}
.quick-links li::before{content:"›";position:absolute;left:0;top:-3px;font-size:16px;color:var(--white)}
.contact{position:absolute;left:768px;top:126px;font-size:11.5px;color:var(--foot-text)}
.contact .firm{font-weight:700;letter-spacing:1px;font-size:11.5px;margin-bottom:22px}
.contact .line{display:flex;gap:12px;margin-bottom:14px;line-height:14px}
.contact svg{flex:none}
.foot-bar{position:absolute;left:0;top:387px;width:1200px;height:87px;background:#2b2b2b;border-top:1px solid #222}
.copyright{position:absolute;left:157px;top:38px;font-size:12px;color:var(--foot-text)}
.socials.bottom{left:934px;top:29px}
.socials.bottom span{background:#8b8b8b}
</style>
</head>
<body>

<header class="site-header">
  <div class="brand"><span class="brand-dot"></span><span>Tavrin Security Services Ltd</span></div>
  <div class="tagline">Standard of Vigilance</div>
  <nav class="main-nav">
    <a>HOME</a><a>ABOUT US</a><a>OUR SECURITY SOLUTIONS</a><a>INDUSTRIES WE SERVE</a><a>CONTACT US</a>
  </nav>
  <div class="socials top"><span></span><span></span><span></span></div>
</header>

<section class="hero" role="img" aria-label="Black and white photo of two business people shaking hands">
  <p class="hero-caption">Security Consultacy is simply dummy text of<br>the printing and typesetting industry.</p>
  <svg class="slide-arrow" style="left:115px" viewBox="0 0 34 34"><circle cx="17" cy="17" r="17" fill="rgba(0,0,0,.35)"/><path d="M20 10 L13 17 L20 24" stroke="#fff" stroke-width="2" fill="none"/></svg>
  <svg class="slide-arrow" style="left:1055px" viewBox="0 0 34 34"><circle cx="17" cy="17" r="17" fill="rgba(0,0,0,.35)"/><path d="M14 10 L21 17 L14 24" stroke="#fff" stroke-width="2" fill="none"/></svg>
</section>

<section class="solutions">
  <h2 class="section-title head-font" style="top:52px">Our Security Solutions</h2>
  <div class="services-nav">
    <h3 class="head-font">Services</h3>
    <ul>
      <li>Property guards</li>
      <li>Corporate events security</li>
      <li>Personal bodyguard for high net worth individuals</li>
      <li>Security consultancy</li>
      <li>Private investigation</li>
    </ul>
  </div>
  <div class="custom-box">
    <p>CUSTOM OPTIONS<br>AVAILABLE</p>
    <div class="box-brand">Tavrin Security Services Ltd</div>
  </div>

  <div class="col-line" style="left:377px"></div>
  <div class="col-line" style="left:601px"></div>
  <div class="col-line" style="left:823px"></div>
  <div class="col-line" style="left:1045px"></div>
  <div class="row-line" style="left:377px;width:224px;top:408px"></div>
  <div class="row-line" style="left:601px;width:222px;top:422px"></div>
  <div class="row-line" style="left:823px;width:222px;top:385px"></div>

  <article class="card" style="left:377px;top:153px">
    <div class="card-photo" role="img" aria-label="Model house held in two hands" style="background:linear-gradient(#8a6d52,#c9b59c)"></div>
    <h4>Property Guards</h4>
    <p>Lorem ipsum dolor sit amet, cons ectetuer adipiscing elit, sed diam nonummy nibh.</p>
    <span class="btn">Read More</span>
  </article>
  <article class="card" style="left:601px;top:153px">
    <div class="card-photo" role="img" aria-label="Bodyguard in dark clothes with arms crossed" style="background:linear-gradient(#3a3f4a,#151820)"></div>
    <h4>Personal Bodyguards</h4>
    <p>Duis autem vel eum iriure dolor i n hendrerit in vulputate velit esse molestie consequat.</p>
    <span class="btn" style="margin-top:24px">Read More</span>
  </article>
  <article class="card" style="left:823px;top:153px">
    <div class="card-photo" role="img" aria-label="Investigator with camera inside a car" style="background:linear-gradient(#6f8aa3,#2c3340)"></div>
    <h4>Private Investigation</h4>
    <p>Ut wisi enim ad minim veniam, qu is nostrud exerci tation ullamcorp er suscipit lobortis</p>
    <span class="btn" style="margin-top:2px">Read More</span>
  </article>
  <article class="card" style="left:377px;top:416px">
    <div class="card-photo" role="img" aria-label="Security staff in jackets at an event" style="background:linear-gradient(#4a4f5a,#1b1e24)"></div>
    <h4>Corporate Events Security</h4>
    <p>Lorem ipsum dolor sit amet, cons ectetuer adipiscing elit, sed diam nonummy nibh euismod tincidunt ut laoreet dolore.</p>
    <span class="btn">Read More</span>
  </article>
  <article class="card" style="left:601px;top:430px">
    <div class="card-photo" role="img" aria-label="Consultants meeting at a table" style="background:linear-gradient(#c8ccd2,#5a5f68)"></div>
    <h4>Security Consultancy</h4>
    <p>Duis autem vel eum iriure dolor in hendrerit in vulputate velit ess e molestie consequat, vel illum d olore eu feugiat nulla.</p>
    <span class="btn" style="margin-top:4px">Read More</span>
  </article>
  <article class="card" style="left:823px;top:393px">
    <div class="card-photo" role="img" aria-label="Protection team beside a black vehicle" style="background:linear-gradient(#7a7f88,#202328)"></div>
    <h4>Executive Protection</h4>
    <p>Lorem ipsum dolor sit amet, cons ectetuer adipiscing elit, sed diam nonummy nibh euismod tincidunt ut laoreet dolore magna aliquam erat volutpat.</p>
    <span class="btn">Read More</span>
  </article>
</section>

<section class="industries">
  <h2 class="section-title head-font" style="top:52px">Industries We Serve</h2>
  <svg class="slide-arrow" style="left:107px" viewBox="0 0 34 34"><circle cx="17" cy="17" r="17" fill="#c4c4c4"/><path d="M20 10 L13 17 L20 24" stroke="#fff" stroke-width="2" fill="none"/></svg>
  <div class="industry" style="left:157px"><div class="ind-photo" role="img" aria-label="Factory with spools and a delivery truck" style="background:linear-gradient(#b58a5c,#5e4a3a)"></div><span>Corporates and Manufacturers</span></div>
  <div class="industry" style="left:387px"><div class="ind-photo" role="img" aria-label="Clothing store interior with shoppers" style="background:linear-gradient(#c79a86,#6a4c48)"></div><span>Retail</span></div>
  <div class="industry" style="left:619px"><div class="ind-photo" role="img" aria-label="Plated food and a glass of wine" style="background:linear-gradient(#e8e4d6,#a2a77a)"></div><span>Food and Beverage</span></div>
  <div class="industry" style="left:849px"><div class="ind-photo" role="img" aria-label="Wall of blue video screens" style="background:linear-gradient(#3c7fb6,#0e2c4c)"></div><span>Entertainment and Media</span></div>
  <svg class="slide-arrow" style="left:1060px" viewBox="0 0 34 34"><circle cx="17" cy="17" r="17" fill="#c4c4c4"/><path d="M14 10 L21 17 L14 24" stroke="#fff" stroke-width="2" fill="none"/></svg>
</section>

<section class="split">
  <div class="split-divider"></div>
  <div class="offer" style="left:130px">
    <div class="ring"><div role="img" aria-label="Resident receiving a parcel at the front door" style="background:linear-gradient(#c9b9a4,#7d6a58)"></div></div>
    <h4>Residential Solutions</h4>
    <p>Lorem ipsum dolor sit amet, consectetur adipiscing elit. Sed in porta ut mauris vitae accumsan. Ut bibendum condim Phasellus placerat lectus nec odio fermentum, non Proin nec ligula condimentum, aliquet nisi id,</p>
    <span class="btn">Read More</span>
  </div>
  <div class="offer" style="left:670px">
    <div class="ring"><div role="img" aria-label="Guard in black uniform beside an office tower" style="background:linear-gradient(#8fb2d4,#2a2d35)"></div></div>
    <h4>Commercial Solutions</h4>
    <p>Lorem ipsum dolor sit amet, consectetur adipiscing elit. Sed in porta ut mauris vitae accumsan. Ut bibendum condim Phasellus placerat lectus nec odio fermentum, non Proin nec ligula condimentum, aliquet nisi id,</p>
    <span class="btn">Read More</span>
  </div>
</section>

<footer class="site-footer">
  <h3 style="left:157px">About us</h3>
  <div class="about-text">
    <p>Lorem ipsum dolor sit amet, consectetur adipiscing elit. Morbi pellentesque iaculis justo eget fermentum. Pellentesque commodo iaculis neque, vitae tincidun odio pellentesque luctus. Aenean in eros eu magna vestibulum imperdiet pretium nec augue.</p>
    <p>Etiam quis turpis enim. Vestibulum auctor id mauris vulputate consequat. Suspendisse potenti. Cras at imperdiet elit. Integer fringilla lectus non diam condimentum, sed ultricies urna ultricies. Sed cong dui quis dui convallis dictum. Donec malesuada vulputate risus vitae vulputate. Maecenas in congue urna. Sed porttitor bibendum</p>
  </div>
  <h3 style="left:542px">Quick Links</h3>
  <ul class="quick-links">
    <li>HOME</li><li>ABOUT US</li><li>OUR SECURITY SOLUTIONS</li><li>INDUSTRIES WE SERVE</li><li>CONTACT US</li>
  </ul>
  <h3 style="left:768px">Contact Us</h3>
  <div class="contact">
    <div class="firm">TAVRIN SECURITY SERVICES LTD.</div>
    <div class="line"><svg width="14" height="18" viewBox="0 0 14 18"><path d="M7 0C3 0 0 3 0 7c0 5 7 11 7 11s7-6 7-11c0-4-3-7-7-7z" fill="#fff"/><circle cx="7" cy="7" r="2.5" fill="#3a3a3a"/></svg><span>12 HARBOUR RD, KELMONT,<br>WELLINGTON 6011, NEW ZEALAND</span></div>
    <div class="line"><svg width="14" height="16" viewBox="0 0 14 16"><path d="M3 0l3 4-2 2c1 2 3 4 5 5l2-2 3 3-2 3C7 15 0 8 0 2z" fill="#fff"/></svg><span>+64 4 555 0192</span></div>
    <div class="line"><svg width="14" height="12" viewBox="0 0 14 12"><rect width="14" height="12" fill="#fff"/><path d="M0 0l7 6 7-6" stroke="#3a3a3a" stroke-width="1.4" fill="none"/></svg><span>info@tavrinsecurity.example</span></div>
  </div>
  <div class="foot-bar">
    <div class="copyright">Copyright © 2014 Tavrin Security Services Ltd.</div>
    <div class="socials bottom"><span></span><span></span><span></span></div>
  </div>
</footer>

</body>
</html>
```